Fitness competition business needs a card design

I need a professional business card design using my logo. The card will be horizontal with rounded edges.

Target Market(s)

Female fitness competitors

Industry/Entity Type

Fitness

Contact Information for Business Card

Lise-Anne Korvath
Owner
stagevelora.com
210.555.0137
info@stagevelora.com

Font styles to use
Serif

Colors

Designer to choose colors to be used in the design.

Requirements
Must have
• On the back please add the following:
• Figure
• Bikini
• Physique
• Fitness
Nice to have
• Looking for a very sleek design, contemporary and easy to read.
Should not have
• Should not be difficult to read or be too busy

```html
<!DOCTYPE html>
<html lang="en">
<head>
<meta charset="UTF-8">
<title>Stage Velora – Business Card</title>
<link href="https://fonts.googleapis.com/css2?family=Noto+Serif:wght@400;700&display=swap" rel="stylesheet">
<style>
  :root {
    --bg-light: #8f9594;
    --bg-dark: #585d5f;
    --card: #ffffff;
    --red: #e52b2c;
    --red-dark: #b51e20;
    --grey: #5a5a5c;
    --grey-dark: #3a3a3c;
    --ink: #3d3d3f;
    --faint: #ededed;
  }
  * { box-sizing: border-box; margin: 0; padding: 0; }
  html, body { width: 1200px; height: 1000px; overflow: hidden; }
  body {
    background: radial-gradient(ellipse at 45% 40%, var(--bg-light), var(--bg-dark));
    font-family: "Noto Serif", Georgia, serif;
    color: var(--ink);
    position: relative;
  }
  .card {
    position: absolute;
    left: 320px;
    width: 560px;
    height: 320px;
    background: var(--card);
    border-radius: 20px;
    overflow: hidden;
    box-shadow: 0 10px 24px rgba(0,0,0,0.35);
  }
  .card--front { top: 150px; }
  .card--back { top: 520px; }
  .card__art { position: absolute; inset: 0; width: 100%; height: 100%; }

  .brand {
    position: absolute;
    left: 0; right: 0; top: 110px;
    text-align: center;
  }
  .brand__mark {
    display: inline-block;
    width: 22px; height: 22px;
    border-radius: 50%;
    background: var(--red);
    vertical-align: middle;
    margin-right: 12px;
  }
  .brand__name {
    font-size: 46px;
    font-weight: 700;
    color: var(--red);
    vertical-align: middle;
    letter-spacing: 1px;
  }
  .brand__rule {
    width: 250px; height: 4px;
    margin: 14px auto 0;
    background: var(--grey);
    box-shadow: 0 9px 0 var(--grey);
  }

  .person__name {
    position: absolute; left: 196px; top: 30px;
    font-size: 25px; line-height: 36px; font-weight: 700; color: var(--ink);
    white-space: nowrap;
  }
  .person__role {
    position: absolute; left: 204px; top: 96px;
    font-size: 16px; line-height: 22px; color: #fff;
  }
  .contacts {
    position: absolute; left: 80px; top: 140px;
    list-style: none; font-size: 18px; line-height: 28px;
  }
  .contacts li { display: flex; align-items: center; white-space: nowrap; }
  .contacts__dot {
    width: 10px; height: 10px; border-radius: 50%;
    border: 2px solid var(--grey); margin-right: 16px;
  }
  .divisions {
    position: absolute; left: 40px; right: 40px; top: 258px;
    display: flex; justify-content: space-between;
    font-size: 20px; line-height: 30px; color: var(--ink);
  }
  .divisions__sep { color: var(--red); }
</style>
</head>
<body>

<section class="card card--front" aria-label="Card front">
  <svg class="card__art" viewBox="0 0 560 320" aria-hidden="true">
    <polygon points="0,90 30,100 30,240 0,250" fill="var(--grey-dark)"/>
    <polygon points="0,110 40,120 40,230 0,240" fill="var(--red)"/>
    <polygon points="560,30 530,40 530,200 560,210" fill="var(--grey-dark)"/>
    <polygon points="560,55 520,65 520,190 560,198" fill="var(--red)"/>
  </svg>
  <div class="brand">
    <span class="brand__mark"></span><span class="brand__name">STAGE VELORA</span>
    <div class="brand__rule"></div>
  </div>
</section>

<section class="card card--back" aria-label="Card back">
  <svg class="card__art" viewBox="0 0 560 320" aria-hidden="true">
    <circle cx="460" cy="170" r="78" fill="var(--faint)"/>
    <polygon points="560,62 150,80 138,94 560,78" fill="var(--red)"/>
    <polygon points="560,78 138,94 133,100 560,84" fill="var(--grey-dark)"/>
    <polygon points="175,24 560,10 560,62 150,80" fill="#fff" stroke="var(--red-dark)" stroke-width="2"/>
    <polygon points="190,92 340,92 352,120 190,120" fill="var(--red)"/>
    <line x1="40" y1="248" x2="520" y2="248" stroke="var(--red)" stroke-width="2"/>
    <line x1="40" y1="298" x2="520" y2="298" stroke="var(--red)" stroke-width="2"/>
  </svg>
  <div class="person__name">Lise-Anne Korvath</div>
  <div class="person__role">Owner</div>
  <ul class="contacts">
    <li><span class="contacts__dot"></span>stagevelora.com</li>
    <li><span class="contacts__dot"></span>210.555.0137</li>
    <li><span class="contacts__dot"></span>info@stagevelora.com</li>
  </ul>
  <div class="divisions">
    <span>Figure</span><span class="divisions__sep">|</span>
    <span>Bikini</span><span class="divisions__sep">|</span>
    <span>Physique</span><span class="divisions__sep">|</span>
    <span>Fitness</span>
  </div>
</section>

</body>
</html>
```